Need a book cover design for book titled: Resting Beside the River--Simple Methods for the Crossing

This book describes and presents tools to connect with and activate the Lightbody that we all carry within us. It talks about the Lighbody, brief history, lightbody levels and offers exercises to bring light into the body.
I envision a design that shows a physical body changing into light /surrounded by light; a resurrected body ascending to higher dimensions of Spirit o anything comparable .
Updates

Target Market(s)

Mature audience of spiritual seekers and those on spiritual path

Requirements
Must have
• Space on backcover for book summary at top and title and author name on spine.

```html
<!DOCTYPE html>
<html lang="en">
<head>
<meta charset="utf-8">
<title>Resting Beside the River — Cover Colourways</title>
<link rel="stylesheet" href="https://fonts.googleapis.com/css2?family=Cinzel+Decorative:wght@700&family=Cinzel:wght@600;700&display=swap">
<style>
  :root {
    --page-bg: #ffffff;
    --title-ink: #f4f1ec;
    --title-shade: #2a2a33;
    --subtitle-ink: #f3dfb8;
    --author-ink: #ffffff;
    --spine-ink: #d9d4cc;

    --ember-core: #fff1c4;
    --ember-glow: #ff9a2e;
    --ember-hot: #ff6a12;
    --ember-deep: #8a3a10;
    --ember-sky: #2a1408;
    --ember-mist: #2b4fc4;
    --ember-cool: #6fb0ff;

    --aurora-core: #e8f4ff;
    --aurora-glow: #5fd6e8;
    --aurora-hot: #4a4fd8;
    --aurora-deep: #3b2a8c;
    --aurora-sky: #140d2e;
    --aurora-mist: #b0307a;
    --aurora-cool: #ff8ccf;
  }
  * { margin: 0; padding: 0; box-sizing: border-box; }
  html, body {
    width: 1200px; height: 900px; overflow: hidden;
    background: var(--page-bg);
  }
  .stage {
    width: 1200px; height: 900px;
    display: flex; justify-content: center; align-items: center; gap: 72px;
  }
  .book {
    display: flex; height: 690px;
    box-shadow: 0 12px 30px rgba(0,0,0,0.25);
  }

  /* Spine */
  .spine {
    position: relative; width: 34px; height: 100%;
    display: flex; flex-direction: column; align-items: center;
    writing-mode: vertical-rl;
    font-family: "Cinzel", serif; color: var(--spine-ink);
    box-shadow: inset -3px 0 6px rgba(0,0,0,0.5);
  }
  .book--ember .spine { background: linear-gradient(180deg, #3a1d10 0%, #1c1212 50%, #0d0c14 100%); }
  .book--aurora .spine { background: linear-gradient(180deg, #231a4a 0%, #1b1030 50%, #0c0818 100%); }
  .spine-author {
    margin-top: 70px;
    font-size: 11px; font-weight: 600; letter-spacing: 2px; text-transform: uppercase;
  }
  .spine-title {
    margin-top: 200px;
    font-family: "Cinzel Decorative", serif; font-weight: 700;
    font-size: 19px; letter-spacing: 2px; white-space: nowrap;
  }

  /* Front cover */
  .cover {
    position: relative; width: 440px; height: 100%; overflow: hidden;
  }
  .cover-sky { position: absolute; inset: 0; }
  .book--ember .cover-sky {
    background:
      radial-gradient(ellipse 20% 60% at 62% 8%, rgba(255,244,220,0.95) 0%, transparent 75%),
      radial-gradient(ellipse 70% 55% at 50% 28%, var(--ember-glow) 0%, var(--ember-deep) 50%, transparent 90%),
      radial-gradient(ellipse 55% 35% at 45% 86%, var(--ember-mist) 0%, transparent 80%),
      linear-gradient(180deg, var(--ember-sky) 0%, #1a0d0a 60%, #0c0a14 100%);
  }
  .book--aurora .cover-sky {
    background:
      radial-gradient(ellipse 20% 60% at 62% 8%, rgba(220,250,255,0.95) 0%, transparent 75%),
      radial-gradient(ellipse 70% 55% at 50% 28%, #6a7de0 0%, var(--aurora-deep) 50%, transparent 90%),
      radial-gradient(ellipse 55% 35% at 45% 88%, var(--aurora-mist) 0%, transparent 80%),
      linear-gradient(180deg, var(--aurora-sky) 0%, #1a0f36 60%, #0c0818 100%);
  }
  .cover-figure {
    position: absolute; left: 105px; top: 290px; width: 250px; height: 400px;
    border-radius: 50% 50% 40% 40% / 30% 30% 70% 70%;
    filter: blur(6px);
  }
  .book--ember .cover-figure {
    background:
      radial-gradient(ellipse 45% 30% at 50% 40%, var(--ember-core) 0%, transparent 100%),
      linear-gradient(180deg, var(--ember-hot) 0%, var(--ember-glow) 40%, var(--ember-mist) 72%, var(--ember-cool) 100%);
    opacity: 0.85;
  }
  .book--aurora .cover-figure {
    background:
      radial-gradient(ellipse 45% 30% at 50% 40%, var(--aurora-core) 0%, transparent 100%),
      linear-gradient(180deg, var(--aurora-hot) 0%, var(--aurora-glow) 40%, #7a5ad8 65%, var(--aurora-cool) 100%);
    opacity: 0.85;
  }

  .cover-title {
    position: absolute; top: 50px; left: 0; right: 0; text-align: center;
    font-family: "Cinzel Decorative", serif; font-weight: 700;
    font-size: 46px; line-height: 1.05; letter-spacing: 1px;
    color: var(--title-ink);
    text-shadow: 0 2px 0 var(--title-shade), 0 4px 6px rgba(0,0,0,0.6);
  }
  .cover-subtitle {
    position: absolute; top: 160px; left: 0; right: 0; text-align: center;
    font-family: "Cinzel", serif; font-weight: 700;
    font-size: 16px; letter-spacing: 1px; text-transform: uppercase;
    color: var(--subtitle-ink);
    text-shadow: 0 1px 3px rgba(0,0,0,0.8);
  }
  .cover-author {
    position: absolute; bottom: 76px; right: 26px;
    font-family: "Cinzel", serif; font-weight: 700;
    font-size: 19px; letter-spacing: 1px; text-transform: uppercase;
    color: var(--author-ink);
    text-shadow: 0 1px 3px rgba(0,0,0,0.8);
  }
</style>
</head>
<body>
  <main class="stage">
    <article class="book book--ember">
      <aside class="spine">
        <span class="spine-author">Author Name</span>
        <span class="spine-title">Resting Beside the River</span>
      </aside>
      <section class="cover">
        <div class="cover-sky" role="img" aria-label="Warm orange light rays and drifting sparks over dark blue mist"></div>
        <div class="cover-figure" role="img" aria-label="Translucent human light body with arms open, glowing orange above and blue below, rising upward"></div>
        <h1 class="cover-title">Resting Beside<br>the River</h1>
        <p class="cover-subtitle">Simple Methods for the Crossing</p>
        <p class="cover-author">Author Name</p>
      </section>
    </article>
    <article class="book book--aurora">
      <aside class="spine">
        <span class="spine-author">Author Name</span>
        <span class="spine-title">Resting Beside the River</span>
      </aside>
      <section class="cover">
        <div class="cover-sky" role="img" aria-label="Cool cyan and violet light rays and drifting sparks over magenta mist"></div>
        <div class="cover-figure" role="img" aria-label="Translucent human light body with arms open, glowing blue and cyan above and pink below, rising upward"></div>
        <h1 class="cover-title">Resting Beside<br>the River</h1>
        <p class="cover-subtitle">Simple Methods for the Crossing</p>
        <p class="cover-author">Author Name</p>
      </section>
    </article>
  </main>
</body>
</html>
```